Icon-Design für Entwicklung von IT-Anwendungen
Zielgruppe
Entwicklung von IT-Anwendungen - Schwerpunkt sind Intranet-Anwendungen
Aufgabenstellung
Modernes Button-Layout mit Fokus auf 'technisches', eher schnörkelloses Design
1. Gewünscht wird ein modernes Layout für 8 Buttons (vgl. alte Buttons in buttons.png). Für jede Aktion (z.B. Einzelprojekt bearbeiten, Speichern, Löschen, usw.) soll ein aussagefähiges Icon und der jeweilige Text enthalten sein.
2. Für jeden Button soll es eine Highlight-Variante geben (für spätere MouseOver-Anwendung)
3. Weiterhin wird eine Leiste gewünscht, in die die Buttons später integriert werden. Als Farbe soll ein Blauton verwendet werden, der zum restlichen Blau harmoniert.
Technische Vorgaben für Buttons
- Größe jeweils 130 x 34 Pixel
- Hintergrundfarbe transparent
- Photoshop-Dateiformat, so dass Texte editierbar bleiben
Technische Vorgaben für Leiste
- Größe 1320 x 40 Pixel
- PNG-Dateiformat

```html
<!DOCTYPE html>
<html lang="de">
<head>
<meta charset="utf-8">
<title>Button-Leiste Projektverwaltung</title>
<link href="https://fonts.googleapis.com/css2?family=PT+Sans:wght@400;700&display=swap" rel="stylesheet">
<style>
  :root{
    --page:#ffffff;
    --bar-top:#e4e4e4;
    --bar-mid:#f3f3f3;
    --bar-bottom:#e2e2e2;
    --btn-top:#fafafa;
    --btn-bottom:#d9d9d9;
    --btn-ring:#f6f6f6;
    --icon:#555555;
    --label:#555555;
    --heading:#a6a6a6;
    --danger:#e01010;
    --accent:#1a64d8;
    --cursor:#000000;
  }
  html,body{margin:0;padding:0;overflow:hidden;background:var(--page);}
  .canvas{position:relative;width:1200px;height:416px;overflow:hidden;background:var(--page);font-family:"PT Sans",sans-serif;}
  .toolbar{position:absolute;left:90px;width:1020px;height:31px;
    background:linear-gradient(to bottom,var(--bar-top),var(--bar-mid) 45%,var(--bar-bottom));}
  .toolbar--default{top:75px;}
  .toolbar--danger{top:248px;}
  .toolbar--accent{top:313px;}
  .btn{position:absolute;top:3px;width:94px;height:25px;border-radius:13px;
    background:linear-gradient(to bottom,var(--btn-top),var(--btn-bottom));
    box-shadow:0 0 0 2px var(--btn-ring),0 2px 2px rgba(0,0,0,.35);
    color:var(--label);}
  .btn__icon{position:absolute;left:8px;top:2px;width:25px;height:21px;color:var(--icon);}
  .btn__label{position:absolute;left:39px;top:4px;font-size:7.4px;line-height:8.6px;white-space:nowrap;}
  .btn--danger,.btn--danger .btn__icon{color:var(--danger);}
  .btn--accent,.btn--accent .btn__icon{color:var(--accent);}
  .btn--danger .btn__label,.btn--accent .btn__label{font-weight:700;}
  .heading{position:absolute;left:95px;top:205px;margin:0;font-size:21px;font-weight:700;color:var(--heading);letter-spacing:.2px;}
  .cursor{position:absolute;width:24px;height:31px;}
  .cursor--danger{left:1087px;top:265px;}
  .cursor--accent{left:306px;top:332px;}
</style>
</head>
<body>
<div class="canvas">
<svg width="0" height="0" style="position:absolute">
  <defs>
    <symbol id="i-new" viewBox="0 0 25 21"><path d="M1 5h7l2 2h9v2H6L3 18H1z" fill="currentColor"/><path d="M6 10h15l-3 9H2z" fill="currentColor"/><path d="M19 1h2v4h4v2h-4v4h-2V7h-4V5h4z" fill="currentColor"/></symbol>
    <symbol id="i-single" viewBox="0 0 25 21"><path d="M3 5h7v15H3z M10 12l-4 8h4z" fill="currentColor"/><circle cx="15" cy="8" r="5" fill="none" stroke="currentColor" stroke-width="2"/><path d="M18 11l5 5-2 2-5-5z" fill="currentColor"/></symbol>
    <symbol id="i-multi" viewBox="0 0 25 21"><path d="M1 5h6l2 2h6v2H5L3 17H1z" fill="currentColor"/><path d="M5 10h10l-2 9H2z" fill="currentColor"/><circle cx="17" cy="9" r="5" fill="none" stroke="currentColor" stroke-width="2"/><path d="M20 12l4 5-2 2-4-5z" fill="currentColor"/></symbol>
    <symbol id="i-edit" viewBox="0 0 25 21"><path d="M9 2l11 4-3 12-10-4z" fill="currentColor"/><path d="M3 10l4-3 9 11-4 3z" fill="currentColor" stroke="var(--btn-top)" stroke-width=".8"/></symbol>
    <symbol id="i-save-prev" viewBox="0 0 25 21"><path d="M2 2h14l4 4v8h-3a5 5 0 0 0-5 5H2z" fill="currentColor"/><path d="M6 2h7v5H6z" fill="var(--btn-top)"/><path d="M10 3h2v3h-2z" fill="currentColor"/><path d="M24 20h-2a3 3 0 0 0-3-3v2l-4-3 4-3v2a5 5 0 0 1 5 5z" fill="currentColor"/></symbol>
    <symbol id="i-save-next" viewBox="0 0 25 21"><path d="M2 2h14l4 4v6h-3a5 5 0 0 0-5 5v2H2z" fill="currentColor"/><path d="M6 2h7v5H6z" fill="var(--btn-top)"/><path d="M10 3h2v3h-2z" fill="currentColor"/><path d="M14 20h2a3 3 0 0 1 3-3v2l4-3-4-3v2a5 5 0 0 0-5 5z" fill="currentColor"/></symbol>
    <symbol id="i-duplicate" viewBox="0 0 25 21"><path d="M4 3h6l2 2h9v2H4z" fill="currentColor"/><path d="M2 6h6l2 2h11v2H5L3 18H2z" fill="currentColor"/><path d="M6 11h18l-3 8H3z" fill="currentColor"/></symbol>
    <symbol id="i-delete" viewBox="0 0 25 21"><path d="M8 3h9v1h4v2H4V4h4z" fill="currentColor"/><path d="M6 7h13l-1 13H7z" fill="currentColor"/><path d="M9 9h1.2v9H9zM12 9h1.2v9H12zM15 9h1.2v9H15z" fill="var(--btn-top)"/></symbol>
    <symbol id="i-cursor" viewBox="0 0 24 31"><path d="M2 2v24l6-6 5 9 4-2-5-9h8z" fill="#fff" stroke="var(--cursor)" stroke-width="2.4" stroke-linejoin="round"/></symbol>
  </defs>
</svg>

<div class="toolbar toolbar--default">
  <div class="btn" style="left:12px"><svg class="btn__icon"><use href="#i-new"/></svg><span class="btn__label">Neues Projekt<br>anlegen</span></div>
  <div class="btn" style="left:141px"><svg class="btn__icon"><use href="#i-single"/></svg><span class="btn__label">Einzelprojekt-<br>ansicht</span></div>
  <div class="btn" style="left:270px"><svg class="btn__icon"><use href="#i-multi"/></svg><span class="btn__label">Multiprojekt-<br>ansicht</span></div>
  <div class="btn" style="left:399px"><svg class="btn__icon"><use href="#i-edit"/></svg><span class="btn__label">Einzelprojekt<br>bearbeiten</span></div>
  <div class="btn" style="left:528px"><svg class="btn__icon"><use href="#i-save-prev"/></svg><span class="btn__label">Speichern und zum<br>letzten Projekt</span></div>
  <div class="btn" style="left:657px"><svg class="btn__icon"><use href="#i-save-next"/></svg><span class="btn__label">Speichern und zum<br>nächsten Projekt</span></div>
  <div class="btn" style="left:786px"><svg class="btn__icon"><use href="#i-duplicate"/></svg><span class="btn__label">Dupliziere<br>dieses Projekt</span></div>
  <div class="btn" style="left:915px"><svg class="btn__icon"><use href="#i-delete"/></svg><span class="btn__label">Lösche<br>dieses Projekt</span></div>
</div>

<h2 class="heading">Rollover-Effekte:</h2>

<div class="toolbar toolbar--danger">
  <div class="btn" style="left:12px"><svg class="btn__icon"><use href="#i-new"/></svg><span class="btn__label">Neues Projekt<br>anlegen</span></div>
  <div class="btn" style="left:141px"><svg class="btn__icon"><use href="#i-single"/></svg><span class="btn__label">Einzelprojekt-<br>ansicht</span></div>
  <div class="btn" style="left:270px"><svg class="btn__icon"><use href="#i-multi"/></svg><span class="btn__label">Multiprojekt-<br>ansicht</span></div>
  <div class="btn" style="left:399px"><svg class="btn__icon"><use href="#i-edit"/></svg><span class="btn__label">Einzelprojekt<br>bearbeiten</span></div>
  <div class="btn" style="left:528px"><svg class="btn__icon"><use href="#i-save-prev"/></svg><span class="btn__label">Speichern und zum<br>letzten Projekt</span></div>
  <div class="btn" style="left:657px"><svg class="btn__icon"><use href="#i-save-next"/></svg><span class="btn__label">Speichern und zum<br>nächsten Projekt</span></div>
  <div class="btn" style="left:786px"><svg class="btn__icon"><use href="#i-duplicate"/></svg><span class="btn__label">Dupliziere<br>dieses Projekt</span></div>
  <div class="btn btn--danger" style="left:915px"><svg class="btn__icon"><use href="#i-delete"/></svg><span class="btn__label">Lösche<br>dieses Projekt</span></div>
</div>

<div class="toolbar toolbar--accent">
  <div class="btn" style="left:12px"><svg class="btn__icon"><use href="#i-new"/></svg><span class="btn__label">Neues Projekt<br>anlegen</span></div>
  <div class="btn btn--accent" style="left:141px"><svg class="btn__icon"><use href="#i-single"/></svg><span class="btn__label">Einzelprojekt-<br>ansicht</span></div>
  <div class="btn" style="left:270px"><svg class="btn__icon"><use href="#i-multi"/></svg><span class="btn__label">Multiprojekt-<br>ansicht</span></div>
  <div class="btn" style="left:399px"><svg class="btn__icon"><use href="#i-edit"/></svg><span class="btn__label">Einzelprojekt<br>bearbeiten</span></div>
  <div class="btn" style="left:528px"><svg class="btn__icon"><use href="#i-save-prev"/></svg><span class="btn__label">Speichern und zum<br>letzten Projekt</span></div>
  <div class="btn" style="left:657px"><svg class="btn__icon"><use href="#i-save-next"/></svg><span class="btn__label">Speichern und zum<br>nächsten Projekt</span></div>
  <div class="btn" style="left:786px"><svg class="btn__icon"><use href="#i-duplicate"/></svg><span class="btn__label">Dupliziere<br>dieses Projekt</span></div>
  <div class="btn" style="left:915px"><svg class="btn__icon"><use href="#i-delete"/></svg><span class="btn__label">Lösche<br>dieses Projekt</span></div>
</div>

<svg class="cursor cursor--danger"><use href="#i-cursor"/></svg>
<svg class="cursor cursor--accent"><use href="#i-cursor"/></svg>
</div>
</body>
</html>
```